Reliable and clean label for a natural product!

We would like to have a label design for our CBD SOFT GEL CAPSULES . We are a business family and believe in the power of natural healing. In this label we would like to show a reliable, natural and feminine product mainly.

Font styles to use
Serif
Sans Serif

Colors

Designer to choose colors to be used in the design.

```html
<!DOCTYPE html>
<html lang="es">
<head>
<meta charset="utf-8">
<title>Serena CBD – Capsule Label</title>
<link href="https://fonts.googleapis.com/css2?family=Montserrat:wght@500&family=Josefin+Sans:wght@400&family=Cabin:wght@700&display=swap" rel="stylesheet">
<style>
  :root{
    --bg:#f3f4f1;
    --label-white:#ffffff;
    --green:#86ad68;
    --green-light:#c3dab0;
    --green-dark:#5c7654;
    --green-rule:#6f9a52;
    --ink:#4a4b4a;
    --on-green:#ffffff;
  }
  *{box-sizing:border-box;margin:0;padding:0}
  html,body{width:1200px;height:780px;overflow:hidden;background:var(--bg)}
  .label{
    position:absolute;left:80px;top:110px;width:1040px;height:560px;
    background:var(--label-white);overflow:hidden;border-radius:6px;
    box-shadow:0 6px 24px rgba(0,0,0,.08);
  }
  .label__waves{position:absolute;inset:0;width:100%;height:100%}
  .label__content{position:absolute;inset:0;display:flex;flex-direction:column;align-items:center}
  .brand{margin-top:34px;display:flex;flex-direction:column;align-items:center}
  .brand__circle{width:78px;height:78px;border:2px solid var(--ink);border-radius:50%}
  .brand__name{
    margin-top:14px;font-family:"Montserrat",sans-serif;font-weight:500;
    font-size:54px;letter-spacing:1px;color:var(--ink);
  }
  .product-box{
    margin-top:26px;width:540px;height:150px;border:2px solid var(--green-rule);
    background:rgba(255,255,255,.9);display:flex;flex-direction:column;align-items:center;justify-content:center;
  }
  .product-box__title{font-family:"Josefin Sans",sans-serif;font-size:34px;color:var(--ink);letter-spacing:1px}
  .product-box__rule{width:300px;height:2px;background:var(--green-rule);margin:14px 0 16px}
  .product-box__sub{font-family:"Cabin",sans-serif;font-weight:700;font-size:26px;color:var(--green-rule)}
  .spec{margin-top:36px;text-align:center;color:var(--on-green)}
  .spec__type{font-family:"Josefin Sans",sans-serif;font-size:32px;letter-spacing:1px}
  .spec__dose{font-family:"Cabin",sans-serif;font-weight:700;font-size:28px;margin-top:4px}
  .count{
    position:absolute;left:0;right:0;top:500px;text-align:center;
    font-family:"Cabin",sans-serif;font-weight:700;font-size:22px;color:var(--on-green);letter-spacing:.5px;
  }
</style>
</head>
<body>
  <div class="label">
    <svg class="label__waves" viewBox="0 0 1040 560" preserveAspectRatio="none" aria-hidden="true">
      <path d="M1040 30 C820 110 720 250 0 250 L0 560 L1040 560 Z" fill="var(--green-light)"/>
      <path d="M0 330 C320 300 720 300 1040 140 L1040 560 L0 560 Z" fill="var(--green)"/>
      <rect x="0" y="468" width="1040" height="18" fill="var(--green-dark)"/>
    </svg>
    <div class="label__content">
      <div class="brand">
        <span class="brand__circle"></span>
        <span class="brand__name">SERENA CBD</span>
      </div>
      <div class="product-box">
        <p class="product-box__title">CAPSULAS ACEITE DE CBD</p>
        <span class="product-box__rule"></span>
        <p class="product-box__sub">Hemp Oil Extract Capsules</p>
      </div>
      <div class="spec">
        <p class="spec__type">FULL SPECTRUM</p>
        <p class="spec__dose">25mg CBD per capsule</p>
      </div>
      <p class="count">30 Capsules</p>
    </div>
  </div>
</body>
</html>
```